Graphic designs required for HR consulting Website

We need to items designed to be used on our website and in presentations.
Please view our website for design ideas.
http://www.vorlimex.com.au.42.plonkhost.pw
See attached Powerpoint doc for more info.
InfoGraphic 1
Needs to be turned into an infographic that will be embedded into the Vorlimex HR website.
The fonts should be Helvetica Neue and should have the look and feel of the website.
InfoGraphic 2
Needs to be turned into an infographic that will be embedded into the Vorlimex HR website and used in PPT and WORD proposals.
The fonts should be Helvetica Neue, the look and
feel should be consistent with the first infographic.
A mountain analogy is needed that shows how the sequence of services will come together to take businesses on the journey to becoming great.
2 versions of the same information are shown on the following slides. The first is for ease of visibility, the second is to show the sequence of services on the journey.
Samples of possible design ideas for inspiration are at bottom of ppt.
Consulting
- Helvetica

```html
<!DOCTYPE html>
<html lang="en">
<head>
<meta charset="utf-8">
<title>Vorlimex HR – The Journey to Greatness</title>
<link rel="stylesheet" href="https://fonts.googleapis.com/css2?family=Oswald:wght@400&family=Roboto:wght@300;700&display=swap">
<style>
  :root {
    --paper: #ffffff;
    --land: #e4e5e6;
    --heading-grey: #76777a;
    --brand-blue: #2b8fd8;
    --deep-navy: #1e3657;
    --bar-light: #d9dadb;
    --bar-dark: #9a9c9f;
    --numeral-grey: #6b6c6f;
    --guide-line: #2b8fd8;
    --dash: #6b6c6f;
  }
  html, body {
    margin: 0;
    padding: 0;
    width: 1200px;
    height: 849px;
    overflow: hidden;
    background: var(--paper);
  }
  .journey {
    display: block;
    width: 1200px;
    height: 849px;
  }
  .stage-title {
    font-family: "Oswald", "Arial Narrow", sans-serif;
    font-weight: 400;
    font-size: 31px;
    fill: var(--heading-grey);
    text-anchor: end;
  }
  .service-title {
    font-family: "Roboto", "Helvetica Neue", Arial, sans-serif;
    font-weight: 700;
    font-size: 15px;
    fill: var(--brand-blue);
  }
  .service-copy {
    font-family: "Roboto", "Helvetica Neue", Arial, sans-serif;
    font-weight: 300;
    font-size: 15px;
    fill: var(--brand-blue);
  }
  .align-end { text-anchor: end; }
  .guide { stroke: var(--guide-line); stroke-width: 0.8; fill: none; }
  .path-dashes { stroke: var(--dash); stroke-width: 2.4; stroke-dasharray: 6 6; fill: none; }
  .connector { stroke: url(#barShade); stroke-width: 9; stroke-linecap: butt; }
  .connector-edge { stroke: #ffffff; stroke-width: 13; }
  .numeral {
    font-family: "Roboto", "Helvetica Neue", Arial, sans-serif;
    font-weight: 700;
    fill: var(--numeral-grey);
    text-anchor: middle;
    dominant-baseline: central;
  }
</style>
</head>
<body>
<svg class="journey" viewBox="0 0 1200 849" xmlns="http://www.w3.org/2000/svg">
  <defs>
    <radialGradient id="landTone" cx="50%" cy="45%" r="60%">
      <stop offset="0" stop-color="#e6e7e8"/>
      <stop offset="0.7" stop-color="#eeeff0"/>
      <stop offset="1" stop-color="#ffffff"/>
    </radialGradient>
    <linearGradient id="barShade" x1="0" y1="0" x2="0" y2="1">
      <stop offset="0" stop-color="#e8e9ea"/>
      <stop offset="0.5" stop-color="#a6a8ab"/>
      <stop offset="1" stop-color="#d0d1d3"/>
    </linearGradient>
    <linearGradient id="barShadeDiag" x1="0" y1="0" x2="1" y2="0">
      <stop offset="0" stop-color="#e8e9ea"/>
      <stop offset="0.5" stop-color="#a6a8ab"/>
      <stop offset="1" stop-color="#d0d1d3"/>
    </linearGradient>
    <radialGradient id="faceShade" cx="45%" cy="35%" r="70%">
      <stop offset="0" stop-color="#ffffff"/>
      <stop offset="0.7" stop-color="#f2f3f4"/>
      <stop offset="1" stop-color="#dcdde0"/>
    </radialGradient>
    <filter id="softShadow" x="-30%" y="-30%" width="160%" height="160%">
      <feDropShadow dx="0" dy="2" stdDeviation="3" flood-color="#000" flood-opacity="0.22"/>
    </filter>

    <symbol id="icon-briefcase" viewBox="-12 -12 24 24">
      <rect x="-11" y="-6" width="22" height="15" rx="1.5" fill="#fff"/>
      <rect x="-4.5" y="-9.5" width="9" height="4.5" rx="1" fill="none" stroke="#fff" stroke-width="1.8"/>
      <line x1="-11" y1="-1" x2="11" y2="-1" stroke="#1e3657" stroke-width="1"/>
    </symbol>
    <symbol id="icon-monitor" viewBox="-12 -12 24 24">
      <rect x="-11" y="-10" width="22" height="15" rx="1.5" fill="none" stroke="#fff" stroke-width="2"/>
      <rect x="-6" y="-4" width="2.2" height="6" fill="#fff"/>
      <rect x="-2.5" y="-6.5" width="2.2" height="8.5" fill="#fff"/>
      <rect x="1" y="-2" width="2.2" height="4" fill="#fff"/>
      <rect x="4.5" y="-3.5" width="2.2" height="5.5" fill="#fff"/>
      <path d="M-5 11 L5 11 L3 5 L-3 5 Z" fill="#fff"/>
    </symbol>
    <symbol id="icon-gears" viewBox="-12 -12 24 24">
      <g transform="translate(3,-3)">
        <circle r="5.8" fill="none" stroke="#fff" stroke-width="3.4" stroke-dasharray="2.6 1.95"/>
        <circle r="5" fill="#fff"/>
        <circle r="1.8" fill="#1e3657"/>
      </g>
      <g transform="translate(-5,5)">
        <circle r="3.8" fill="none" stroke="#fff" stroke-width="2.6" stroke-dasharray="2 1.58"/>
        <circle r="3.2" fill="#fff"/>
        <circle r="1.2" fill="#1e3657"/>
      </g>
    </symbol>

    <g id="service-node">
      <circle r="31" fill="#fff" filter="url(#softShadow)"/>
      <circle r="27" fill="var(--deep-navy)"/>
      <circle r="24.5" fill="none" stroke="var(--brand-blue)" stroke-width="1.6"/>
    </g>
  </defs>

  <rect class="map-backdrop" x="50" y="30" width="1100" height="720" rx="40" fill="url(#landTone)" role="img" aria-label="Faint grey world map spread behind the journey"/>

  <!-- guide lines from stage titles to milestones -->
  <g class="guides">
    <polyline class="guide" points="470,80 800,80 846,128"/>
    <polyline class="guide" points="422,210 704,210 736,240"/>
    <polyline class="guide" points="294,362 576,362 604,388"/>
    <polyline class="guide" points="157,506 464,506 486,534"/>
    <polyline class="guide" points="54,761 296,761 318,734"/>
  </g>

  <!-- dashed journey path -->
  <line class="path-dashes" x1="380" y1="737" x2="889" y2="142"/>

  <!-- connectors -->
  <g class="connectors">
    <line class="connector-edge" x1="618" y1="280" x2="901" y2="280"/>
    <line class="connector" x1="618" y1="280" x2="901" y2="280"/>
    <line class="connector-edge" x1="498" y1="417" x2="781" y2="417"/>
    <line class="connector" x1="498" y1="417" x2="781" y2="417"/>
    <line class="connector-edge" x1="381" y1="577" x2="662" y2="577"/>
    <line class="connector" x1="381" y1="577" x2="662" y2="577"/>
    <line x1="525" y1="577" x2="665" y2="686" stroke="#fff" stroke-width="13"/>
    <line x1="525" y1="577" x2="665" y2="686" stroke="url(#barShadeDiag)" stroke-width="9"/>
  </g>

  <!-- milestones -->
  <g class="milestones">
    <g class="milestone" transform="translate(380,737)">
      <circle r="62" fill="#fff" filter="url(#softShadow)"/>
      <circle r="55" fill="var(--deep-navy)"/>
      <circle r="49" fill="var(--brand-blue)"/>
      <circle r="45" fill="url(#faceShade)"/>
      <text class="numeral" font-size="44">1</text>
    </g>
    <g class="milestone" transform="translate(525,577)">
      <circle r="57" fill="#fff" filter="url(#softShadow)"/>
      <circle r="50" fill="var(--deep-navy)"/>
      <circle r="45" fill="var(--brand-blue)"/>
      <circle r="41" fill="url(#faceShade)"/>
      <text class="numeral" font-size="40">2</text>
    </g>
    <g class="milestone" transform="translate(645,420)">
      <circle r="53" fill="#fff" filter="url(#softShadow)"/>
      <circle r="46" fill="var(--deep-navy)"/>
      <circle r="42" fill="var(--brand-blue)"/>
      <circle r="38" fill="url(#faceShade)"/>
      <text class="numeral" font-size="38">3</text>
    </g>
    <g class="milestone" transform="translate(765,280)">
      <circle r="50" fill="#fff" filter="url(#softShadow)"/>
      <circle r="44" fill="var(--deep-navy)"/>
      <circle r="40" fill="var(--brand-blue)"/>
      <circle r="36" fill="url(#faceShade)"/>
      <text class="numeral" font-size="36">4</text>
    </g>
    <g class="milestone" transform="translate(889,142)">
      <circle r="46" fill="#fff" filter="url(#softShadow)"/>
      <circle r="40" fill="var(--deep-navy)"/>
      <circle r="36" fill="var(--brand-blue)"/>
      <circle r="32" fill="url(#faceShade)"/>
      <text class="numeral" font-size="32">5</text>
    </g>
  </g>

  <!-- service nodes -->
  <g class="service-nodes">
    <g transform="translate(618,280)"><use href="#service-node"/><use href="#icon-briefcase" x="-12" y="-12" width="24" height="24"/></g>
    <g transform="translate(901,280)"><use href="#service-node"/><use href="#icon-briefcase" x="-12" y="-12" width="24" height="24"/></g>
    <g transform="translate(498,417)"><use href="#service-node"/><use href="#icon-monitor" x="-12" y="-12" width="24" height="24"/></g>
    <g transform="translate(781,417)"><use href="#service-node"/><use href="#icon-monitor" x="-12" y="-12" width="24" height="24"/></g>
    <g transform="translate(381,577)"><use href="#service-node"/><use href="#icon-gears" x="-12" y="-12" width="24" height="24"/></g>
    <g transform="translate(662,577)"><use href="#service-node"/><use href="#icon-gears" x="-12" y="-12" width="24" height="24"/></g>
    <g transform="translate(665,686)"><use href="#service-node"/><use href="#icon-gears" x="-12" y="-12" width="24" height="24"/></g>
  </g>

  <!-- stage titles -->
  <g class="stage-titles">
    <text class="stage-title" x="792" y="76" textLength="286" lengthAdjust="spacingAndGlyphs">THE EMBEDDING GREATNESS</text>
    <text class="stage-title" x="698" y="204" textLength="246" lengthAdjust="spacingAndGlyphs">DEVELOPING GREATNESS</text>
    <text class="stage-title" x="574" y="356" textLength="250" lengthAdjust="spacingAndGlyphs">RESOURCING GREATNESS</text>
    <text class="stage-title" x="458" y="500" textLength="264" lengthAdjust="spacingAndGlyphs">THE HEART OF GREATNESS</text>
    <text class="stage-title" x="290" y="720" textLength="184" lengthAdjust="spacingAndGlyphs">THE FOUNDATIONS</text>
    <text class="stage-title" x="290" y="754" textLength="147" lengthAdjust="spacingAndGlyphs">OF GREATNESS</text>
  </g>

  <!-- stage descriptions -->
  <g class="stage-copy">
    <text class="service-copy align-end" x="790" y="102">ON-SITE STRATEGIC AND OPERATIONAL</text>
    <text class="service-copy align-end" x="790" y="121">SUPPORT TO SUSTAIN YOUR JOURNEY</text>
    <text class="service-copy align-end" x="288" y="784">TRUSTED ADVICE AND</text>
    <text class="service-copy align-end" x="288" y="800">COMPLIANCE SUPPORT</text>
  </g>

  <!-- services -->
  <g class="services">
    <text class="service-title align-end" x="574" y="270">DEVELOP STAR PLAYERS</text>
    <text class="service-copy align-end" x="574" y="290">LEADERSHIP COACHING</text>

    <text class="service-title" x="949" y="270">CREATE STAR TEAMS</text>
    <text class="service-copy" x="949" y="290">LEADERSHIP</text>
    <text class="service-copy" x="949" y="305">DEVELOPMENT PROGRAMS</text>

    <text class="service-title align-end" x="454" y="403">CULTURAL X-RAY</text>
    <text class="service-copy align-end" x="454" y="423">PRE-EMPLOYMENT</text>
    <text class="service-copy align-end" x="454" y="438">ASSESSMENTS</text>

    <text class="service-title" x="829" y="407">RECRUIT ASSIST</text>
    <text class="service-copy" x="829" y="427">THE EXPERTISE TO SELECT</text>
    <text class="service-copy" x="829" y="443">GREAT PEOPLE</text>

    <text class="service-title align-end" x="337" y="556">STEP 1: DEFINING GREATNESS</text>
    <text class="service-copy align-end" x="337" y="576">BUSINESS STRATEGY, KPLS,</text>
    <text class="service-copy align-end" x="337" y="593">BEHAVIOURS AND ROLE</text>
    <text class="service-copy align-end" x="337" y="610">CLARITY</text>

    <text class="service-title" x="709" y="564">STEP 2: MEASURING GREATNESS</text>
    <text class="service-copy" x="709" y="584">CREATING A CULTURE</text>
    <text class="service-copy" x="709" y="602">OF ACCOUNTABILITY</text>

    <text class="service-title" x="706" y="676">STEP 3: REWARDING GREATNESS</text>
    <text class="service-copy" x="706" y="696">REMUNERATION AND</text>
    <text class="service-copy" x="706" y="713">INCENTIVE SCHEMES</text>
  </g>
</svg>
</body>
</html>
```